Etiketten-Design für österreichischen Qualitätswein gesucht
Zielgruppe
Der Name unseres Weingutes ist HALLER. Wir produzieren österreichische Qualitätsweine und vermarkten diese unter dem Namen HALLER.
Die Weine werden über den Lebensmitteleinzelhandel vertrieben und sollen ein urbanes Publikum zum Impulskauf ansprechen. Es sollte eine grafische Darstellung von einem Fuchs vorkommen. Es kann natürlich Stockmaterial verwendet werden. Das Etikett kann seriös, lustig oder frech sein. Es kann zum Beispiel eine bekannte Fabel mit einem Fuchs darstellen.
Aufgabenstellung
Maximale Höhe: 10,5cm
Papierfarbe: weiß
Folgende Angaben sind am Etikett erforderlich:
- Name: HALLER
- Weinsorte: SAUVIGNON BLANC
- Herkunft: BURGENLAND - ÖSTERREICH

```html
<!DOCTYPE html>
<html lang="de">
<head>
<meta charset="utf-8">
<title>HALLER – Sauvignon Blanc Etikett</title>
<link rel="stylesheet" href="https://fonts.googleapis.com/css2?family=Bebas+Neue&family=Crimson+Pro:wght@500&display=swap">
<style>
  :root {
    --wine-red: #7a0000;
    --ink: #141414;
    --paper: #ffffff;
    --stage: #ffffff;
    --illustration-light: #e9e9e9;
    --illustration-dark: #8a8a8a;
  }
  html, body {
    margin: 0;
    padding: 0;
    width: 1200px;
    height: 600px;
    overflow: hidden;
    background: var(--stage);
  }
  .stage {
    position: relative;
    width: 1200px;
    height: 600px;
  }
  .label {
    position: absolute;
    left: 397px;
    top: 30px;
    width: 405px;
    height: 540px;
    background: var(--paper);
    box-shadow: 6px 8px 18px rgba(0, 0, 0, 0.22);
    overflow: hidden;
  }
  .label-frame {
    position: absolute;
    left: 11px;
    top: 9px;
    width: 385px;
    height: 520px;
    border: 2.5px solid var(--wine-red);
    box-sizing: border-box;
  }
  .fox-illustration {
    position: absolute;
    left: 140px;
    top: 82px;
    width: 230px;
    height: 344px;
    background: radial-gradient(ellipse at 55% 55%, var(--illustration-dark) 0%, #b5b5b5 45%, var(--illustration-light) 80%, rgba(255,255,255,0) 100%);
    opacity: 0.7;
  }
  .brand-name {
    position: absolute;
    left: 30px;
    top: 32px;
    width: 345px;
    margin: 0;
    text-align: center;
    white-space: nowrap;
    font-family: "Bebas Neue", "Oswald", sans-serif;
    font-weight: 400;
    font-size: 146px;
    line-height: 1;
    color: var(--wine-red);
    letter-spacing: 0;
    mix-blend-mode: multiply;
  }
  .vintage-badge {
    position: absolute;
    left: 40px;
    top: 202px;
    width: 94px;
    height: 94px;
    border-radius: 50%;
    background: var(--ink);
    color: var(--paper);
    display: flex;
    align-items: center;
    justify-content: center;
    font-family: "Bebas Neue", "Oswald", sans-serif;
    font-size: 36px;
    letter-spacing: 0.06em;
    padding-top: 3px;
    box-sizing: border-box;
  }
  .variety-band {
    position: absolute;
    left: 0;
    top: 426px;
    width: 405px;
    height: 44px;
    background: var(--wine-red);
    color: var(--paper);
    display: flex;
    align-items: center;
    justify-content: center;
    font-family: "Crimson Pro", "Times New Roman", serif;
    font-weight: 500;
    font-size: 21px;
    letter-spacing: 0.34em;
    padding-left: 0.34em;
    box-sizing: border-box;
  }
  .origin {
    position: absolute;
    left: 0;
    top: 487px;
    width: 405px;
    text-align: center;
    font-family: "Bebas Neue", "Oswald", sans-serif;
    font-size: 17px;
    color: var(--ink);
    letter-spacing: 1.55em;
    padding-left: 1.55em;
    box-sizing: border-box;
  }
</style>
</head>
<body>
  <main class="stage">
    <article class="label">
      <div class="label-frame"></div>
      <div class="fox-illustration" role="img" aria-label="Schwarz-weiße Federzeichnung eines sitzenden Fuchses"></div>
      <h1 class="brand-name">HALLER</h1>
      <div class="vintage-badge">2010</div>
      <div class="variety-band">SAUVIGNON BLANC</div>
      <div class="origin">BURGENLAND</div>
    </article>
  </main>
</body>
</html>
```